Erklär-Flyer für Gutschein-Ankauf-Service Bonkarten-Profi.de
Zielgruppe
Auf http://www.bonkarten-profi.de/ bieten wir u.a. den Service an, ungenutzte Geschenkkarten von großen Händlern wie z.B. Technoplatz, Vandoro, WOLM, usw. direkt gegen Bargeld einzutauschen. Diesen Service wollen wir nun in einem Flyer vorstellen.
Die Zielgruppe des zu erstellenden Flyers sollen vor allem Mitarbeiter bei Firmen z.B. Auto Verkäufer sein, die von Ihrem Arbeitgeber als Prämie Geschenkgutscheine als Incentive erhalten und diese aber lieber in Bargeld umtauschen würden.
Das Wunschszenario wäre: Wir schicken den Flyer zusammen mit einem Anschreiben an die jeweiligen Firmen. Der/diejenige die den Brief und Flyer entgegennimmt, erkennt den Sinn und Nutzen und gibt den Flyer an Ihre Kollegen weiter bzw. hängt ihn ans schwarze Brett etc.
Aufgabenstellung
Gestaltet werden soll ein 3 Schritte Falz-Flyer (z.B. 6-seitiger Altarfalz Fensterfalz) angelehnt an das bisherige Design auf Bonkarten-Profi.de (nicht zwingend 100%, gerne auch eigene Ideen). Auf der Außenseite nur kurz in einem Satz um was es geht und auf der Innenseite dann am Besten in 3 Schritten erklärt, wie einfach der Umtausch von Gutscheinen in Bargeld ist.
Das Wichtigste ist die "Bequemlichkeit, Einfachheit, kein Aufwand", am zweitwichtigsten ist "Sicherheit, Seriosität" (Unsere Seite gibt es schon seit 2008 und wir wurden bereits im KRT vorgestellt).
Verteilung des Falt-Flyer als Brief mit der Post. Wenn der Brief geöffnet wird ist der zu erreichende Optimal Zustand, dass der Flyer von der Person, die den Brief öffnet, z.B. ans "schwarze Brett" gehängt wird als Info bzw. eine Art Anleitung.

```html
<!DOCTYPE html>
<html lang="de">
<head>
<meta charset="utf-8">
<title>Bonkarten-Profi.de – Falzflyer</title>
<link rel="stylesheet" href="https://fonts.googleapis.com/css2?family=Arimo:wght@400;700&display=swap">
<style>
  :root {
    --blue: #2b4fa0;
    --blue-text: #3056a8;
    --green: #9bc232;
    --white: #ffffff;
    --ink: #222222;
    --page: #ffffff;
  }
  * { box-sizing: border-box; margin: 0; padding: 0; }
  html, body { width: 1200px; height: 447px; overflow: hidden; background: var(--page); }
  body { font-family: "Arimo", Arial, sans-serif; position: relative; }

  .spread-inside { position: absolute; left: 3px; top: 4px; width: 617px; height: 437px; overflow: hidden; }
  .backdrop { position: absolute; inset: 0; background: linear-gradient(120deg, #f4efe9 0%, #ebe3db 35%, #f5f3f1 60%, #e8e9ec 100%); }

  .claim-circle { position: absolute; left: 182px; top: -33px; width: 112px; height: 112px; border-radius: 50%; background: var(--blue); color: var(--white); text-align: center; padding-top: 50px; }
  .claim-circle .small { font-size: 11px; display: block; }
  .claim-circle .big { font-size: 16px; display: block; line-height: 1.1; }

  .brand { position: absolute; font-weight: 700; color: var(--blue); line-height: 1.05; }
  .brand--inside { left: 531px; top: 23px; font-size: 11px; }

  .intro { position: absolute; left: 267px; top: 55px; width: 171px; padding: 4px 7px; background: rgba(255,255,255,.75); color: var(--blue-text); font-size: 8.4px; line-height: 1.3; text-align: justify; }
  .intro b { font-weight: 700; }

  .steps { position: absolute; left: 0; top: 146px; }

  .num { position: absolute; width: 54px; height: 54px; border-radius: 50%; background: var(--green); color: var(--white); font-weight: 700; font-size: 36px; text-align: center; line-height: 54px; }

  .providers { position: absolute; left: 3px; top: 152px; width: 130px; font-size: 4px; color: var(--ink); }
  .providers h3 { font-size: 6.5px; font-weight: 700; }
  .providers h3 span { background: #000; color: #fff; padding: 0 1px; margin-right: 2px; }
  .providers p { margin: 2px 0 6px; font-size: 3.6px; }
  .providers ul { list-style: none; columns: 3; column-gap: 4px; }
  .providers li { color: var(--blue); line-height: 8px; }
  .providers li::before { content: "➜ "; }

  .form { position: absolute; left: 146px; top: 152px; width: 294px; font-size: 6px; color: var(--ink); }
  .form .radio { display: flex; align-items: center; gap: 3px; height: 10px; padding-left: 0; }
  .form .radio i { width: 6px; height: 6px; border: 1px solid #888; border-radius: 50%; display: inline-block; }
  .form .radio i.on { background: radial-gradient(circle, var(--blue) 40%, #fff 45%); }
  .form .row { position: relative; height: 15.7px; font-weight: 700; font-size: 5.8px; padding-left: 14px; line-height: 10px; }
  .form .row:first-of-type { margin-top: 4px; }
  .form .field { position: absolute; left: 141px; top: 2px; width: 67px; height: 8px; border: 1px solid #888; background: #fff; }
  .form .field.focus { border-color: #5b9bd5; }
  .form .field.wide { left: 225px; }
  .form .note { position: absolute; left: 0; top: 153px; font-size: 5.8px; font-family: "Tinos", "Times New Roman", serif; width: 294px; border-top: 1px solid #ccc; padding-top: 2px; }

  .photo { position: absolute; }
  .photo--step3 { left: 478px; top: 160px; width: 139px; height: 157px; background: linear-gradient(160deg, #f2efec 0%, #c9a58a 45%, #3b2a22 100%); }

  .step-text { position: absolute; top: 335px; font-size: 8.4px; line-height: 1.3; color: var(--blue-text); }
  .step-text b { font-weight: 700; }
  .step-text--1 { left: 14px; }
  .step-text--2 { left: 269px; }
  .step-text--3 { left: 472px; }

  .cover { position: absolute; left: 775px; top: 4px; width: 309px; height: 437px; overflow: hidden; }
  .photo--cover { inset: 0; background: linear-gradient(135deg, #dfe6ea 0%, #e9d4c0 35%, #caa07f 55%, #8a6c5a 80%, #b9b4b0 100%); }
  .brand--cover { left: 12px; top: 20px; font-size: 18px; }
  .promise { position: absolute; left: -4px; top: 96px; width: 84px; height: 84px; border-radius: 50%; background: var(--green); color: var(--white); font-size: 13px; line-height: 1.35; padding: 20px 0 0 14px; }
  .headline-box { position: absolute; left: 168px; top: 295px; width: 124px; height: 100px; background: rgba(255,255,255,.85); text-align: right; padding: 10px 8px 0 0; color: var(--blue-text); }
  .headline-box .lead { display: block; font-size: 12px; line-height: 1.25; text-align: left; padding-left: 8px; }
  .headline-box .main { display: block; font-size: 19px; font-weight: 700; line-height: 1.15; margin-top: 8px; color: var(--blue); }
  .badge { position: absolute; left: 241px; top: 264px; width: 70px; height: 70px; border-radius: 50%; background: var(--green); color: var(--white); font-size: 10px; text-align: center; padding-top: 24px; line-height: 1.25; }
</style>
</head>
<body>

<section class="spread-inside">
  <div class="backdrop" role="img" aria-label="Blasses Hintergrundfoto einer lächelnden Frau mit Einkaufstüten"></div>

  <div class="claim-circle"><span class="small">Unser Vorteil ist</span><span class="big">Ihr Vorteil!</span></div>
  <div class="brand brand--inside">Bonkarten-<br>Profi</div>

  <p class="intro">Mit unserem <b>Ankaufspreis-Rechner</b> sehen sie sofort wie viel Sie für Ihren Gutschein bekommen und können diesen per <b>Sofortverkauf</b> in eine neue Form der Kaufkraft umwandeln.*</p>

  <svg class="steps" width="620" height="180" viewBox="0 0 620 180">
    <polygon points="-2,4 132,4 152,86 132,174 -2,174" fill="#fff" stroke="#9bc232" stroke-width="3"/>
    <polygon points="142,4 440,4 466,89 440,174 142,174 164,89" fill="#fff" stroke="#9bc232" stroke-width="3"/>
    <polygon points="452,4 622,4 622,174 452,174 476,89" fill="#fff" stroke="#9bc232" stroke-width="3"/>
  </svg>

  <div class="providers">
    <h3><span>1</span>Anbieter auswählen</h3>
    <p>Wählen Sie zunächst einen der folgenden Anbieter</p>
    <ul>
      <li>Altero</li><li>Vandoro</li><li>Arvi</li><li>Bergmo</li><li>Brilo</li><li>Bunti</li><li>Calvo</li><li>Cerno</li>
      <li>Dorna</li><li>Elvio</li><li>Fenko</li><li>Galo</li><li>Gemi</li><li>WOLM</li><li>Hanso</li><li>Ilvo</li>
      <li>Jasto</li><li>Kelo</li><li>Lumo</li><li>Marvi</li><li>Technoplatz</li><li>Nesto</li><li>Orla</li><li>Pando</li>
    </ul>
  </div>

  <div class="form">
    <div class="radio"><i></i>Ja, ich habe bereits ein Konto und möchte mich einloggen.</div>
    <div class="radio"><i class="on"></i>Ich bin ein neuer Kunde und möchte meine Daten nun eingeben.</div>
    <div class="row">E-Mailadresse<span class="field"></span></div>
    <div class="row">Passwort wählen<span class="field"></span></div>
    <div class="row">Passwort bestätigen <small>(erneut)</small><span class="field"></span></div>
    <div class="row">Vorname<span class="field"></span></div>
    <div class="row">Nachname<span class="field"></span></div>
    <div class="row">Straße und Hausnr.<span class="field focus"></span></div>
    <div class="row">PLZ und Ort<span class="field"></span><span class="field wide"></span></div>
    <div class="row">Ihre Telefonnummer<span class="field"></span></div>
    <p class="note">Wir zahlen Ihr Guthaben nach Eingang des Gutscheins innerhalb von einer Woche auf Ihr Konto aus</p>
  </div>

  <div class="photo photo--step3" role="img" aria-label="Foto einer jungen Frau, die lächelnd Geldscheine hochhält"></div>

  <div class="num" style="left:69px;top:110px">1</div>
  <div class="num" style="left:212px;top:312px">2</div>
  <div class="num" style="left:476px;top:110px">3</div>

  <p class="step-text step-text--1">Wählen Sie auf Unserer Website<br><b>www.bonkarten-profi.de</b><br>Ihren Geschenkanbieter aus.</p>
  <p class="step-text step-text--2">Melden Sie sich <b>kostenlos</b> an und geben<br>Sie Ihre Gutschein-Informationen ein</p>
  <p class="step-text step-text--3">Ausdrucken und den Gutschein<br>an uns senden. Das Geld erhalten<br>Sie <b>direkt auf ihr Konto.</b></p>
</section>

<section class="cover">
  <div class="photo photo--cover" role="img" aria-label="Foto einer lächelnden blonden Frau mit Einkaufstüten über der Schulter"></div>
  <div class="brand brand--cover">Bonkarten-Profi</div>
  <div class="promise">einfach.<br>schnell.<br>seriös.</div>
  <div class="headline-box">
    <span class="lead">Machen Sie<br>ungenutze</span>
    <span class="main">Gutscheine<br>zu Geld</span>
  </div>
  <div class="badge">Bekannt aus<br>dem KRT</div>
</section>

</body>
</html>
```